fieldscoutingpath.com - Social Media Branding

fieldscoutingpath.com --> Social Media Re-Branding & Graphics
Facebook: @fldscoutpath - Instagram: @fieldscoutingpath - Twitter: @fldscoutpath

Looking to find a good designer to help with my fieldscoutingpath.com social media sites!
- facebook banner
- twitter banner
- instagram template (square and banner size)
- Quote or Information Template
- Committed Template (uniformed) - see the ones I made (& i am no professional) at fieldscoutingpath.com/committed - needs to have fieldscoutingpath.com logo, room for: the committed school and the team the player plays on.

Also willing to pay extra for a graphic that is the "complete package" that detail all of the steps of the recruiting process detailed in fieldscoutingpath.com

Font styles to use
Sans Serif

Colors
ec1f27
fbee3e

```html
<!DOCTYPE html>
<html lang="en">
<head>
<meta charset="utf-8">
<title>fieldscoutingpath.com – Coupon Posts</title>
<link rel="stylesheet" href="https://fonts.googleapis.com/css2?family=Barlow:wght@300;400;500;600;700;900&display=swap">
<style>
  :root {
    --red: #bd1e2e;
    --yellow: #eeee50;
    --white: #ffffff;
    --ink: #141414;
    --page: #ffffff;
  }
  * { margin: 0; padding: 0; box-sizing: border-box; }
  html, body {
    width: 1200px; height: 900px; overflow: hidden;
    background: var(--page);
    font-family: "Barlow", Arial, sans-serif;
  }
  .board { position: relative; width: 1200px; height: 900px; }

  .post {
    position: absolute; top: 208px;
    width: 488px; height: 488px; overflow: hidden;
    box-shadow: 6px 8px 14px rgba(0,0,0,0.28);
  }
  .post--yellow { left: 79px; background: var(--yellow); --accent: var(--yellow); --band: var(--red); --headline: var(--white); --stitch-top: var(--yellow); --cta-text: var(--white); }
  .post--white  { left: 640px; background: var(--white);  --accent: var(--yellow); --band: var(--yellow); --headline: var(--red); --stitch-top: var(--red); --cta-text: var(--yellow); }

  .seams { position: absolute; inset: 0; width: 488px; height: 488px; }

  .post__tagline {
    position: absolute; top: 14px; left: 0; width: 100%;
    text-align: center; font-size: 16.5px; font-weight: 500;
    line-height: 21px; color: var(--headline);
  }

  .offer {
    position: absolute; left: 38px; top: 148px;
    font-weight: 900; color: var(--red);
    font-size: 112px; line-height: 98px; letter-spacing: 3px;
  }
  .post--yellow .offer { text-shadow: 6px 6px 0 var(--white); }
  .post--white .offer { text-shadow: 6px 6px 0 var(--yellow); }

  .divider {
    position: absolute; left: 288px; top: 150px;
    width: 2px; height: 187px; background: var(--red);
  }

  .details { position: absolute; left: 312px; top: 168px; }
  .details__label { font-size: 20.5px; font-weight: 400; color: var(--ink); line-height: 24px; letter-spacing: 0.5px; }
  .details__code { font-size: 20.5px; font-weight: 600; color: var(--red); line-height: 26px; }
  .details__note { margin-top: 16px; font-size: 14.5px; font-weight: 400; color: var(--ink); line-height: 17.5px; }
  .cta {
    display: inline-block; margin-top: 14px;
    width: 113px; height: 29px; line-height: 29px;
    background: var(--red); color: var(--cta-text);
    text-align: center; font-size: 13.5px; font-weight: 700; letter-spacing: 1.6px;
  }

  .brand {
    position: absolute; left: 144px; top: 432px;
    display: flex; align-items: center; gap: 12px;
  }
  .brand__mark { width: 26px; height: 26px; border-radius: 50%; background: var(--yellow); }
  .post--yellow .brand__mark { background: var(--red); }
  .brand__name {
    font-size: 19px; font-weight: 700; color: var(--ink);
    padding-bottom: 3px; border-bottom: 1.5px solid var(--red);
    line-height: 20px;
  }
</style>
</head>
<body>
<main class="board">

  <section class="post post--yellow">
    <svg class="seams" viewBox="0 0 488 488" aria-hidden="true">
      <path d="M0 0 H488 V30 Q244 150 0 30 Z" fill="var(--red)"/>
      <path d="M0 42 Q244 162 488 42" fill="none" stroke="var(--yellow)" stroke-width="6"/>
      <path d="M0 446 Q244 376 488 446 V488 H0 Z" fill="var(--white)"/>
      <path d="M0 432 Q244 358 488 432" fill="none" stroke="var(--red)" stroke-width="6"/>
    </svg>
    <p class="post__tagline">In 2019, our students received<br>over $2 million dollars in scholarships!</p>
    <div class="offer">30%<br>OFF</div>
    <div class="divider"></div>
    <div class="details">
      <p class="details__label">COUPON CODE:</p>
      <p class="details__code">CP101</p>
      <p class="details__note">Step-by-Step<br>Recruiting Process</p>
      <span class="cta">JOIN TODAY</span>
    </div>
    <div class="brand">
      <span class="brand__mark"></span>
      <span class="brand__name">fieldscoutingpath.com</span>
    </div>
  </section>

  <section class="post post--white">
    <svg class="seams" viewBox="0 0 488 488" aria-hidden="true">
      <path d="M0 0 H488 V30 Q244 150 0 30 Z" fill="var(--yellow)"/>
      <path d="M0 42 Q244 162 488 42" fill="none" stroke="var(--red)" stroke-width="6"/>
      <path d="M0 432 Q244 358 488 432" fill="none" stroke="var(--red)" stroke-width="6"/>
    </svg>
    <p class="post__tagline">In 2019, our students received<br>over $2 million dollars in scholarships!</p>
    <div class="offer">30%<br>OFF</div>
    <div class="divider"></div>
    <div class="details">
      <p class="details__label">COUPON CODE:</p>
      <p class="details__code">CP101</p>
      <p class="details__note">Step-by-Step<br>Recruiting Process</p>
      <span class="cta">JOIN TODAY</span>
    </div>
    <div class="brand">
      <span class="brand__mark"></span>
      <span class="brand__name">fieldscoutingpath.com</span>
    </div>
  </section>

</main>
</body>
</html>
```